HARBORVALE BANK Stationery and BRAND ARCHITECTURE

We need a unique Design and Architecture for:

a. Business Card
b. Letterhead
c. Continuation Sheet
d. Envelope
e. Email Signature
f. Complimentary Slip
g. Poster
h. Corporate Folder

1. Information for the call card:

Merrick J. Palworth
Senior Assistant Managing Director
General Banking Division
Harborvale Bank
P.O. Box 718, Quillon Street, Basseterre, St. Kitts, West Indies
Office.: (869) 555-0148 Ext 2207
M.: (869) 555-0193
F.: (869) 555-0172
Email: merrickpalworth@harborvalebankexample.com
harborvale.example

2. All pieces must include:
a. Address
b. Contact info
c.twitter and Facebook address

The Information for the posters:
Visual:A Happy Black Family
Headline Our future together – Better!
Bold Our People know how to build for the long term. How to root the future firmly in the strengths of our people.
A vault we can trust for brighter days!

Target Market(s)

BUSiness
Bank Customers

Industry/Entity Type

Bank

Requirements
Must have
• - Logo wiht tag
• - use of Logo Colours
• - Green and Red as main colours but the yellow and black are also important
• - the red circles MUSt be used inthe brand architecture

```html
<!DOCTYPE html>
<html lang="en">
<head>
<meta charset="utf-8">
<title>Harborvale Bank – Business Card</title>
<link rel="stylesheet" href="https://fonts.googleapis.com/css2?family=Source+Sans+3:wght@400;600;700&display=swap">
<style>
  :root {
    --bank-green: #0f5a2c;
    --bank-red: #be1e2d;
    --bank-yellow: #e3ae1b;
    --card-white: #f4f4f2;
    --backdrop: #a4a4a4;
    --ink-light: #ffffff;
  }
  * { margin: 0; padding: 0; box-sizing: border-box; }
  html, body {
    width: 1105px; height: 1200px; overflow: hidden;
    background: var(--backdrop);
    font-family: "Source Sans 3", "Myriad Pro", Arial, sans-serif;
  }
  .sheet { position: relative; width: 1105px; height: 1200px; }
  .card {
    position: absolute; left: 180px; width: 746px; height: 424px;
    background: var(--card-white); overflow: hidden;
  }
  .card--front { top: 120px; }
  .card--back { top: 636px; }

  .card-waves { position: absolute; left: 0; top: 0; }

  .wordmark {
    position: absolute; display: flex; align-items: center; gap: 12px;
    color: var(--bank-green); font-weight: 700; letter-spacing: -0.5px;
  }
  .wordmark-dot { border-radius: 50%; background: var(--bank-red); flex: none; }
  .card--front .wordmark { left: 0; right: 0; justify-content: center; top: 96px; font-size: 50px; }
  .card--front .wordmark-dot { width: 26px; height: 26px; }
  .card--back .wordmark { left: 0; right: 0; justify-content: center; top: 168px; font-size: 54px; }
  .card--back .wordmark-dot { width: 32px; height: 32px; }

  .holder {
    position: absolute; right: 429px; top: 262px; text-align: right;
    color: var(--ink-light); font-size: 16px; line-height: 23px;
  }
  .holder-name { color: var(--bank-yellow); font-size: 25px; font-weight: 600; line-height: 30px; margin-bottom: 4px; }
  .holder-address { margin-top: 13px; }

  .divider {
    position: absolute; left: 335px; top: 272px; width: 1px; height: 118px;
    background: rgba(255,255,255,0.55);
  }

  .contacts { position: absolute; left: 352px; top: 261px; list-style: none; color: var(--ink-light); font-size: 16.5px; }
  .contacts li { display: flex; align-items: center; height: 28.5px; gap: 10px; }
  .contacts svg { width: 18px; height: 18px; flex: none; fill: var(--bank-yellow); }

  .social {
    position: absolute; left: 0; right: 0; top: 360px;
    display: flex; justify-content: center; align-items: center; gap: 6px;
    color: #3b3b3b; font-size: 18px;
  }
  .social-dot { width: 26px; height: 26px; border-radius: 50%; background: var(--bank-green); }
  .social-handle { margin-left: 4px; }
</style>
</head>
<body>
<main class="sheet">

  <section class="card card--front" aria-label="Business card front">
    <svg class="card-waves" width="746" height="424" viewBox="0 0 746 424" aria-hidden="true">
      <path d="M0 200 C140 214 300 236 430 238 C300 240 140 236 0 232 Z" fill="var(--bank-red)"/>
      <path d="M310 240 C480 228 640 206 746 196 L746 214 C640 222 480 236 310 240 Z" fill="var(--bank-yellow)"/>
      <path d="M0 234 C140 240 260 248 340 247 C480 245 640 226 746 218 L746 424 L0 424 Z" fill="var(--bank-green)"/>
    </svg>

    <div class="wordmark"><span class="wordmark-dot"></span>Harborvale Bank</div>

    <div class="holder">
      <p class="holder-name">Merrick J. Palworth</p>
      <p>Senior Assistant Managing Director</p>
      <p>General Banking Division</p>
      <p class="holder-address">P.O. Box 718, Quillon Street</p>
      <p>Basseterre, St. Kitts, West Indies</p>
    </div>

    <div class="divider"></div>

    <ul class="contacts">
      <li><svg viewBox="0 0 24 24" aria-label="Office"><path d="M6.6 10.8a15.1 15.1 0 0 0 6.6 6.6l2.2-2.2c.3-.3.7-.4 1-.2 1.1.4 2.3.6 3.6.6.6 0 1 .4 1 1V20c0 .6-.4 1-1 1A17 17 0 0 1 3 4c0-.6.4-1 1-1h3.5c.6 0 1 .4 1 1 0 1.3.2 2.5.6 3.6.1.3 0 .7-.2 1z"/></svg>(869) 555-0148 Ext 2207</li>
      <li><svg viewBox="0 0 24 24" aria-label="Mobile"><path d="M7 1h10a2 2 0 0 1 2 2v18a2 2 0 0 1-2 2H7a2 2 0 0 1-2-2V3a2 2 0 0 1 2-2zm0 3v14h10V4zm5 15.2a1.2 1.2 0 1 0 0 2.4 1.2 1.2 0 0 0 0-2.4z"/></svg>(869) 555-0193</li>
      <li><svg viewBox="0 0 24 24" aria-label="Fax"><path d="M6 2h9l3 3v4H6zM3 10h18a1 1 0 0 1 1 1v8a1 1 0 0 1-1 1H3a1 1 0 0 1-1-1v-8a1 1 0 0 1 1-1zm3 3v2h12v-2zm0 4v1h12v-1z"/></svg>(869) 555-0172</li>
      <li><svg viewBox="0 0 24 24" aria-label="Email"><path d="M2 5h20v14H2zm2 2v.4l8 5.2 8-5.2V7z"/></svg>merrickpalworth@harborvalebankexample.com</li>
      <li><svg viewBox="0 0 24 24" aria-label="Website"><path d="M12 2a10 10 0 1 0 0 20 10 10 0 0 0 0-20zm-1 17.9A8 8 0 0 1 4.2 10L9 14.8v1a2 2 0 0 0 2 2zm6.9-2.5A2 2 0 0 0 16 16h-1v-3a1 1 0 0 0-1-1H8v-2h2a1 1 0 0 0 1-1V7h2a2 2 0 0 0 2-2v-.4a8 8 0 0 1 2.9 12.8z"/></svg>www.harborvalebankexample.com</li>
    </ul>
  </section>

  <section class="card card--back" aria-label="Business card back">
    <div class="wordmark"><span class="wordmark-dot"></span>Harborvale Bank</div>
    <div class="social">
      <span class="social-dot"></span>
      <span class="social-dot"></span>
      <span class="social-handle">harborvale.example</span>
    </div>
  </section>

</main>
</body>
</html>
```